Compass of Quiet Mornings book cover design

Book cover - the book contains 52 chapters - 2 for each letter of the alphabet, so a yearlong focus on Leadership. The Intent is to communicate that leadership is common sense. It just isn’t common practice. This book allows the reader to focus on one leadership word each week for a yearlong focus on improving one’s leadership. It is full of stories relating to the 52 words that will challenge and inspire the reader.
Target Market(s)
Leaders / Emerging Leaders
Industry/Entity Type
All
Requirements
Must have
- Appeal to executives
Nice to have
- Simplicity
Should not have
- Cartoon feel

```html
<!DOCTYPE html>
<html lang="en">
<head>
<meta charset="utf-8">
<title>Compass of Quiet Mornings – Book Cover</title>
<link rel="stylesheet" href="https://fonts.googleapis.com/css2?family=Oswald:wght@600&family=Playfair+Display:wght@400&display=swap">
<style>
  :root {
    --backdrop: #ebe5da;
    --navy: #16202b;
    --spine: #0f171f;
    --gold: #e3ad3b;
    --red: #b63a2e;
    --teal: #3f6a80;
    --cream: #eee4d3;
    --brown: #6b3a22;
    --bar-cream: #ebd9c8;
  }
  * { margin: 0; padding: 0; box-sizing: border-box; }
  html, body { width: 1200px; height: 1200px; overflow: hidden; background: var(--backdrop); }
  .cover {
    position: absolute; left: 180px; top: 40px;
    width: 840px; height: 1120px;
    background: var(--navy);
    box-shadow: 0 10px 30px rgba(0,0,0,.25);
  }
  .spine { position: absolute; left: 0; top: 0; width: 38px; height: 100%; background: var(--spine); }
  .rule { position: absolute; background: var(--gold); }
  .rule--spine { left: 72px; top: 0; width: 5px; height: 100%; }
  .rule--top { left: 122px; top: 44px; width: 665px; height: 5px; }
  .rule--lower { left: 122px; top: 960px; width: 665px; height: 5px; }
  .rule--base { left: 122px; top: 1068px; width: 665px; height: 5px; }

  .tile-mosaic { position: absolute; inset: 0; }
  .tile { position: absolute; }
  .t-gold { background: var(--gold); }
  .t-red { background: var(--red); }
  .t-teal { background: var(--teal); }
  .t-cream { background: var(--cream); }
  .t-brown { background: var(--brown); }

  .title { position: absolute; color: var(--gold); white-space: nowrap; }
  .title__main {
    left: 226px; top: 282px;
    font-family: "Oswald", sans-serif; font-weight: 600;
    font-size: 88px; letter-spacing: 20px; line-height: 1;
  }
  .title__serif { font-family: "Playfair Display", serif; font-weight: 400; line-height: 1; }
  .title__of { left: 250px; top: 378px; font-size: 80px; }
  .title__quiet { left: 278px; top: 478px; font-size: 70px; }
  .title__mornings { left: 226px; top: 560px; font-size: 84px; }

  .crown-ornament {
    position: absolute; left: 372px; top: 392px; width: 190px; height: 48px;
    background: var(--gold); opacity: .85;
    clip-path: polygon(0 100%, 100% 100%, 100% 60%, 0 60%);
  }
  .title-swoosh { position: absolute; left: 330px; top: 440px; }

  .bar { position: absolute; border-radius: 4px; }
  .bar--gold { left: 207px; top: 657px; width: 410px; height: 88px; background: var(--gold); }
  .bar--cream { left: 221px; top: 861px; width: 443px; height: 80px; background: var(--bar-cream); }

  .author {
    position: absolute; left: 0; width: 100%; top: 985px;
    display: flex; justify-content: center; align-items: center; gap: 34px;
    padding-left: 60px;
    color: var(--gold);
    font-family: "Playfair Display", serif; font-size: 52px; letter-spacing: 4px;
  }
  .author__star { width: 34px; height: 34px; fill: var(--gold); }
</style>
</head>
<body>
<main class="cover">
  <div class="spine"></div>
  <div class="rule rule--spine"></div>
  <div class="rule rule--top"></div>

  <div class="tile-mosaic" role="img" aria-label="Mosaic of framed alphabet tiles and small vintage illustrations bordering the title">
    <span class="tile t-teal"  style="left:122px;top:63px;width:70px;height:90px"></span>
    <span class="tile t-gold"  style="left:196px;top:63px;width:70px;height:90px"></span>
    <span class="tile t-teal"  style="left:270px;top:63px;width:70px;height:90px"></span>
    <span class="tile t-red"   style="left:344px;top:63px;width:70px;height:90px"></span>
    <span class="tile t-gold"  style="left:418px;top:63px;width:70px;height:90px"></span>
    <span class="tile t-gold"  style="left:492px;top:63px;width:70px;height:90px"></span>
    <span class="tile t-teal"  style="left:566px;top:63px;width:70px;height:90px"></span>
    <span class="tile t-red"   style="left:640px;top:63px;width:70px;height:90px"></span>
    <span class="tile t-red"   style="left:714px;top:63px;width:73px;height:90px"></span>
    <span class="tile t-cream" style="left:122px;top:161px;width:70px;height:90px"></span>
    <span class="tile t-red"   style="left:196px;top:161px;width:70px;height:90px"></span>
    <span class="tile t-gold"  style="left:270px;top:161px;width:70px;height:90px"></span>
    <span class="tile t-brown" style="left:344px;top:161px;width:70px;height:90px"></span>
    <span class="tile t-teal"  style="left:418px;top:161px;width:70px;height:90px"></span>
    <span class="tile t-gold"  style="left:492px;top:161px;width:70px;height:90px"></span>
    <span class="tile t-red"   style="left:566px;top:161px;width:70px;height:90px"></span>
    <span class="tile t-teal"  style="left:640px;top:161px;width:70px;height:90px"></span>
    <span class="tile t-gold"  style="left:122px;top:260px;width:70px;height:120px"></span>
    <span class="tile t-teal"  style="left:122px;top:387px;width:70px;height:120px"></span>
    <span class="tile t-red"   style="left:122px;top:514px;width:70px;height:120px"></span>
    <span class="tile t-cream" style="left:122px;top:641px;width:70px;height:100px"></span>
    <span class="tile t-brown" style="left:594px;top:380px;width:60px;height:78px"></span>
    <span class="tile t-gold"  style="left:660px;top:380px;width:60px;height:78px"></span>
    <span class="tile t-brown" style="left:632px;top:465px;width:70px;height:74px"></span>
    <span class="tile t-cream" style="left:707px;top:465px;width:74px;height:74px"></span>
    <span class="tile t-teal"  style="left:632px;top:545px;width:70px;height:95px"></span>
    <span class="tile t-gold"  style="left:707px;top:545px;width:74px;height:95px"></span>
    <span class="tile t-brown" style="left:632px;top:646px;width:70px;height:104px"></span>
    <span class="tile t-teal"  style="left:707px;top:646px;width:74px;height:104px"></span>
    <span class="tile t-cream" style="left:122px;top:758px;width:70px;height:92px"></span>
    <span class="tile t-teal"  style="left:196px;top:758px;width:70px;height:92px"></span>
    <span class="tile t-gold"  style="left:270px;top:758px;width:70px;height:92px"></span>
    <span class="tile t-teal"  style="left:344px;top:758px;width:70px;height:92px"></span>
    <span class="tile t-brown" style="left:418px;top:758px;width:70px;height:92px"></span>
    <span class="tile t-red"   style="left:492px;top:758px;width:70px;height:92px"></span>
    <span class="tile t-cream" style="left:566px;top:758px;width:70px;height:92px"></span>
    <span class="tile t-gold"  style="left:640px;top:758px;width:70px;height:92px"></span>
    <span class="tile t-teal"  style="left:122px;top:858px;width:70px;height:88px"></span>
    <span class="tile t-brown" style="left:688px;top:858px;width:96px;height:88px"></span>
  </div>

  <h1>
    <span class="title title__main">COMPASS</span>
    <span class="title title__serif title__of">of</span>
    <span class="title title__serif title__quiet">Quiet</span>
    <span class="title title__serif title__mornings">Mornings</span>
  </h1>

  <div class="crown-ornament" role="img" aria-label="Gold crown ornament above the title underline"></div>
  <svg class="title-swoosh" width="245" height="30" viewBox="0 0 245 30" aria-hidden="true">
    <path d="M4 24 Q120 4 240 12" stroke="var(--gold)" stroke-width="7" fill="none" stroke-linecap="round"/>
  </svg>

  <div class="bar bar--gold"></div>
  <div class="bar bar--cream"></div>

  <div class="rule rule--lower"></div>
  <p class="author">
    <svg class="author__star" viewBox="0 0 24 24" aria-hidden="true"><path d="M12 2l2.9 6.9 7.1.6-5.4 4.7 1.6 7.3L12 17.8 5.8 21.5l1.6-7.3L2 9.5l7.1-.6z"/></svg>
    <span class="author__name">AUTHOR NAME</span>
    <svg class="author__star" viewBox="0 0 24 24" aria-hidden="true"><path d="M12 2l2.9 6.9 7.1.6-5.4 4.7 1.6 7.3L12 17.8 5.8 21.5l1.6-7.3L2 9.5l7.1-.6z"/></svg>
  </p>
  <div class="rule rule--base"></div>
</main>
</body>
</html>
```